Solar Cleaning Business Wrap on 2000 F250

Brightwater Solar Cleaning is a specialized service aimed at maintaining and optimizing the performance of solar panels for homeowners and businesses. The primary service offered is the thorough cleaning of solar panels to ensure they operate at maximum efficiency. By removing dust, dirt, bird droppings, and other debris, Brightwater Solar Cleaning helps clients maximize their solar energy production, leading to lower energy bills. Additionally, the business does a lot of Bird Proofing, along with Roof Pressure Washing and Gutter Cleaning as of right now.
When it comes to design, it's crucial to convey professionalism and reliability. Keep it clean, modern, and professional. The design should reflect the precision and attention to detail that characterizes the service. Choose clear, legible fonts that complement the overall design aesthetic and are easy to read across different platforms. Avoid overly ornate fonts that may detract from the message or make the content difficult to understand.
Overall, the design should be visually appealing, informative, and consistent with the brand identity of Brightwater Solar Cleaning. It should effectively communicate the benefits of the service and resonate with the target audience, ultimately driving engagement and conversions.
We love the idea of doing a bold color on the front such as Orange and have it transition to Blue, but also want to see other suggestions/ideas. I want a full wrap on the truck and have it stand out in a good way. Still want it to look sleek and cool. I have attached all of the files for my logo. If you need anything else let me know.
Look forward to all of your ideas/designs.

Target Market(s)

The target market for Brightwater Solar Cleaning comprises homeowners and businesses who have invested in solar panel installations. Homeowners who are looking to protect their investment while also saving money on energy costs are a key demographic. Similarly, businesses that prioritize sustainability and wish to optimize the performance of their solar energy systems would also be part of the target audience.

Industry/Entity Type

Solar Cleaning

Colors
0054AA
0677BA
7BADD7
CADEEF
E8F1F8
F0912C
F2A743
F7CA91
FBE8D2
FDF5EE
EE7325
F08F49
F5BC92
FAE3D3
FDF4ED

Requirements
Must have
• Services provided.
Nice to have
• Black base color. Services provided on rear tailgate.
Should not have
• I would prefer the base color not to be white.

```html
<!DOCTYPE html>
<html lang="en">
<head>
<meta charset="utf-8">
<title>Brightwater Solar Cleaning – Truck Wrap Side Panel</title>
<link rel="stylesheet" href="https://fonts.googleapis.com/css2?family=Oswald:wght@500&family=Poppins:wght@600;800&display=swap">
<style>
  :root {
    --canvas: #ffffff;
    --wrap-black: #0b0b0b;
    --wrap-orange: #f0912c;
    --accent-gold: #f2a743;
    --accent-blue: #3d8fd6;
    --text-light: #ffffff;
  }
  html, body {
    margin: 0;
    width: 1200px;
    height: 1200px;
    overflow: hidden;
    background: var(--canvas);
  }
  .wrap-panel {
    position: absolute;
    left: 40px;
    top: 400px;
    width: 1120px;
    height: 400px;
    overflow: hidden;
  }
  .wrap-panel svg { position: absolute; inset: 0; }
  .service-list {
    position: absolute;
    left: 18px;
    top: 116px;
    margin: 0;
    width: 360px;
    font-family: "Oswald", sans-serif;
    font-weight: 500;
    color: var(--accent-gold);
    font-size: 14px;
    line-height: 1.3;
    letter-spacing: 0.2px;
    text-transform: uppercase;
    text-align: center;
    white-space: nowrap;
    transform: rotate(2.2deg);
    transform-origin: left top;
  }
  .brand-mark {
    position: absolute;
    left: 392px;
    top: 150px;
    display: flex;
    align-items: center;
    gap: 18px;
    transform: rotate(2.6deg);
    transform-origin: left center;
  }
  .brand-dot {
    width: 96px;
    height: 96px;
    border-radius: 50%;
    background: var(--accent-gold);
    flex: none;
  }
  .brand-name {
    font-family: "Poppins", sans-serif;
    font-weight: 800;
    font-size: 38px;
    line-height: 1.05;
    color: var(--accent-blue);
    white-space: nowrap;
  }
  .website {
    position: absolute;
    right: 26px;
    top: 150px;
    margin: 0;
    font-family: "Poppins", sans-serif;
    font-weight: 600;
    font-size: 17px;
    color: var(--text-light);
    white-space: nowrap;
    transform: rotate(2.6deg);
    transform-origin: right center;
  }
</style>
</head>
<body>
  <section class="wrap-panel" aria-label="Truck wrap side layout">
    <svg viewBox="0 0 1120 400" width="1120" height="400" aria-hidden="true">
      <defs>
        <linearGradient id="orangeBase" x1="0" y1="0" x2="1" y2="0">
          <stop offset="0" stop-color="#f0912c"/>
          <stop offset="1" stop-color="#f2a743"/>
        </linearGradient>
      </defs>
      <rect class="base-orange" x="0" y="0" width="1120" height="400" fill="url(#orangeBase)"/>
      <polygon class="top-stripe-blue" points="0,70 1120,122 1120,138 0,86" fill="var(--accent-blue)"/>
      <polygon class="main-band-black" points="0,88 1120,140 1120,330 800,305 350,275 0,250" fill="var(--wrap-black)"/>
      <polygon class="rear-stripe-blue" points="0,190 250,196 300,240 0,228" fill="var(--accent-blue)"/>
      <polygon class="front-stripe-blue" points="780,154 1120,168 1120,196 780,180" fill="var(--accent-blue)"/>
    </svg>

    <p class="service-list">
      Solar Panel Cleaning<br>
      Roof Pressure Washing • Pigeon Proofing/Protective Barrier
    </p>

    <div class="brand-mark">
      <span class="brand-dot"></span>
      <span class="brand-name">Brightwater<br>Solar Cleaning</span>
    </div>

    <p class="website">brightwatersolarcleaning.com</p>
  </section>
</body>
</html>
```